high end contractor

high end contracting company we do all phases of construction kitchen,bathrooms,etc... please look at my website before you design www.harborkeybuild.com

would love some sort of lines or logo or both

Industry/Entity Type

Construction

Contact Information for Business Card

company name: oak & meridian contracting address: 318 fenwick st mount Vernon ny 10552 email: harborkeybuild@mailbrook.com website: www.harborkeybuild.com office#: 914-208-3916 fax#: 914-208-5523 dominic valtersen mobile# 917-526-0389

```html
<!DOCTYPE html>
<html lang="en">
<head>
<meta charset="utf-8">
<title>Oak &amp; Meridian Contracting – Business Card</title>
<link rel="stylesheet" href="https://fonts.googleapis.com/css2?family=Montserrat:wght@300;400;700&family=Open+Sans:wght@300;400;600&display=swap">
<style>
  :root {
    --stage: #e4e5e6;
    --charcoal: #2d2d2f;
    --band: rgba(45, 45, 47, 0.92);
    --teal: #3fbfbc;
    --white: #ffffff;
    --muted: #c9c9c9;
    --ink: #2a2a2a;
    --photo-light: #f2f2f2;
    --photo-mid: #b9b9b9;
    --photo-dark: #3a3a3a;
  }
  * { box-sizing: border-box; margin: 0; padding: 0; }
  html, body { width: 1200px; height: 777px; overflow: hidden; }
  body {
    background: var(--stage);
    position: relative;
    font-family: "Open Sans", sans-serif;
  }
  .card {
    position: absolute;
    top: 234px;
    width: 540px;
    height: 309px;
    overflow: hidden;
    box-shadow: 0 6px 18px rgba(0, 0, 0, 0.18);
  }
  /* Front side */
  .card-front { left: 40px; background: var(--photo-light); }
  .site-photo {
    position: absolute; inset: 0;
    background: linear-gradient(160deg, var(--photo-light) 0%, var(--photo-mid) 45%, var(--photo-light) 62%, var(--photo-dark) 100%);
  }
  .title-band {
    position: absolute; left: 0; right: 0; top: 44px; height: 62px;
    background: var(--band);
    display: flex; align-items: center; justify-content: center; gap: 10px;
    font-family: "Montserrat", sans-serif; font-size: 27px; letter-spacing: 1px;
    text-transform: uppercase;
  }
  .title-band .firm { color: var(--teal); font-weight: 700; }
  .title-band .trade { color: var(--white); font-weight: 300; }
  .social-row {
    position: absolute; top: 138px; left: 0; right: 0;
    display: flex; justify-content: center; gap: 14px;
  }
  .social-dot { width: 30px; height: 30px; border-radius: 50%; background: var(--teal); }
  .web-address {
    position: absolute; top: 190px; left: 0; right: 0; text-align: center;
    font-family: "Open Sans", sans-serif; font-size: 19px; color: var(--ink);
    font-weight: 400; letter-spacing: 0.5px;
  }
  /* Back side */
  .card-back { left: 620px; background: var(--charcoal); }
  .edge-stripe { position: absolute; left: 0; top: 0; bottom: 0; width: 14px; background: var(--teal); }
  .contact-block { position: absolute; left: 230px; top: 60px; color: var(--white); }
  .person-name {
    font-family: "Montserrat", sans-serif; font-weight: 300; font-size: 22px;
    color: var(--teal); text-transform: uppercase; letter-spacing: 0.5px;
  }
  .company-short { font-size: 11px; margin-top: 2px; }
  .address { margin-top: 22px; font-size: 12px; line-height: 1.45; }
  .channels { margin-top: 18px; list-style: none; }
  .channel { display: flex; align-items: center; gap: 9px; font-size: 12px; margin-bottom: 8px; }
  .channel-badge {
    width: 19px; height: 19px; border-radius: 50%; background: var(--teal);
    color: var(--white); font-size: 10px; font-weight: 600;
    display: flex; align-items: center; justify-content: center;
  }
  .channel-email { color: var(--muted); }
</style>
</head>
<body>
  <section class="card card-front">
    <div class="site-photo" role="img" aria-label="Black and white photograph of a construction site"></div>
    <h1 class="title-band"><span class="firm">Oak &amp; Meridian</span><span class="trade">Contracting</span></h1>
    <div class="social-row">
      <span class="social-dot"></span>
      <span class="social-dot"></span>
      <span class="social-dot"></span>
      <span class="social-dot"></span>
    </div>
    <p class="web-address">http://www.harborkeybuild.com</p>
  </section>

  <section class="card card-back">
    <div class="edge-stripe"></div>
    <div class="contact-block">
      <h2 class="person-name">Dominic Valtersen</h2>
      <p class="company-short">Oak &amp; Meridian</p>
      <p class="address">318 Fenwick Street<br>Harlow Point, NY 10947</p>
      <ul class="channels">
        <li class="channel"><span class="channel-badge">E</span><span class="channel-email">harborkeybuild@mailbrook.com</span></li>
        <li class="channel"><span class="channel-badge">P</span><span>914-208-3916</span></li>
        <li class="channel"><span class="channel-badge">F</span><span>914-208-5523</span></li>
        <li class="channel"><span class="channel-badge">M</span><span>917-526-0389</span></li>
      </ul>
    </div>
  </section>
</body>
</html>
```